FREE DENTURES

The card will be placed on plastic stand at doctors office and Seniors centers. This is to acheive specific market segment of people that must have Pelsund A & B card and FULL halvora.
The size of the card shuold be 3.1/2" X 6" printed on vertical format. The basic design must have a picture of a denture and a eye glass frame.The content should be:
NEED DENTURES and/or EYE GLASSES?
NO COST TO YOU
Must have PELSUND A & B and FULL HALVORA
Must qualify for program
No obligation Call today
BRAM OKAFU 706-555-0183
(Not affiliated with Northgate Civic Authority, the Federal Pelsund or the State Halvora Program

Add at a proper side or top. 2 stripes, 1 Red, 1 blue in a waive format.

```html
<!DOCTYPE html>
<html lang="en">
<head>
<meta charset="utf-8">
<title>Need Dentures or Eye Glasses – Program Card</title>
<link rel="stylesheet" href="https://fonts.googleapis.com/css2?family=Fira+Sans+Extra+Condensed:wght@400;600;700&display=swap">
<style>
  :root {
    --page-bg: #ececec;
    --card-bg: #ffffff;
    --brand-red: #e41e26;
    --brand-blue: #3a57a7;
    --ink-grey: #4a4a4a;
    --photo-light: #f4f2f2;
    --photo-warm: #e9b4ad;
  }
  html, body {
    margin: 0;
    width: 1022px;
    height: 1200px;
    overflow: hidden;
    background: var(--page-bg);
  }
  .program-card {
    position: absolute;
    left: 184px;
    top: 40px;
    width: 653px;
    height: 1120px;
    background: var(--card-bg);
    box-shadow: 0 2px 10px rgba(0,0,0,0.12);
  }
  .program-card svg { display: block; width: 100%; height: 100%; }
  .card-text {
    font-family: "Fira Sans Extra Condensed", "Arial Narrow", sans-serif;
    text-anchor: middle;
  }
  .headline { font-weight: 700; }
  .red { fill: var(--brand-red); }
  .blue { fill: var(--brand-blue); }
  .grey { fill: var(--ink-grey); }
  .small-caps { font-variant: small-caps; }
  .regular { font-weight: 400; }
  .contact { font-weight: 700; }
  .disclaimer { font-weight: 400; font-variant: small-caps; }
</style>
</head>
<body>
  <div class="program-card">
    <svg viewBox="0 0 616 1057" xmlns="http://www.w3.org/2000/svg">
      <defs>
        <linearGradient id="product-photo-tone" x1="0" y1="0" x2="1" y2="1">
          <stop offset="0" stop-color="var(--photo-light)"/>
          <stop offset="0.6" stop-color="#f3e6e4"/>
          <stop offset="1" stop-color="var(--photo-warm)"/>
        </linearGradient>
      </defs>

      <!-- top wave stripes -->
      <g class="wave-top">
        <path class="blue" d="M0 0 H490 C390 38 220 52 0 30 Z"/>
        <path class="red" d="M0 36 C140 64 300 66 432 38 C300 78 130 80 0 50 Z"/>
      </g>

      <!-- headline -->
      <g class="card-text headline">
        <text class="red" x="308" y="159" font-size="84" textLength="492" lengthAdjust="spacingAndGlyphs">NEED DENTURES</text>
        <text class="blue" x="301" y="232" font-size="84" textLength="486" lengthAdjust="spacingAndGlyphs"><tspan font-size="58">OR </tspan>EYE GLASSES?</text>
      </g>

      <!-- product photo area -->
      <g class="product-photo" role="img" aria-label="Photo of black rectangular eyeglass frames beside a set of dentures">
        <rect x="36" y="256" width="516" height="222" rx="6" fill="url(#product-photo-tone)"/>
      </g>

      <!-- offer -->
      <g class="card-text">
        <text x="310" y="557" font-size="106" class="regular" textLength="520" lengthAdjust="spacingAndGlyphs"><tspan class="red">NO COST </tspan><tspan class="blue">TO YOU</tspan></text>
        <text class="grey regular small-caps" x="312" y="622" font-size="52">Must have</text>
        <text class="blue regular" x="312" y="692" font-size="56" textLength="384" lengthAdjust="spacingAndGlyphs">PELSUND A &amp; B <tspan class="small-caps" font-size="56">and</tspan></text>
        <text class="blue regular" x="312" y="761" font-size="56">FULL HALVORA</text>
        <text class="grey regular small-caps" x="312" y="828" font-size="66" textLength="542" lengthAdjust="spacingAndGlyphs">Must qualify for program</text>
        <text class="regular small-caps" x="306" y="877" font-size="42" textLength="346" lengthAdjust="spacingAndGlyphs"><tspan class="blue">No obligation </tspan><tspan class="red">Call today</tspan></text>
        <text class="red contact" x="295" y="929" font-size="48" textLength="456" lengthAdjust="spacingAndGlyphs">BRAM OKAFU 706-555-0183</text>
        <text class="ink grey disclaimer" x="307" y="961" font-size="16" textLength="572" lengthAdjust="spacingAndGlyphs">Not affiliated with Northgate Civic Authority, the Federal Pelsund or the State Halvora Program</text>
      </g>

      <!-- bottom wave stripes -->
      <g class="wave-bottom">
        <path class="red" d="M178 1022 C330 972 500 972 616 1008 V1020 C500 990 330 990 178 1022 Z"/>
        <path class="blue" d="M118 1057 C300 1012 480 1010 616 1032 V1057 Z"/>
      </g>
    </svg>
  </div>
</body>
</html>
```